Talvin Crestline Homes needs a business card

We need a business card for a new company in Canada, Ontario. Our company is all about luxury contraction homes for our clients. Our product and services are custom projects design. Under the business logo that will be created, we want a slogan that will be a memorable phrase for consumers to remember us to tell their friends and relatives.

Additional infomation
- Brennick Solvadeu
- President / Ceo
-415.390.7628

Find point what luxury construction products and services can be done

We like to see colors:
- #663300
- and something other colors or color that would attract the client needs and wants

The final design should communicate leads from new or old clients that will grow our empire. Most of all, we try to work among the budget that clients want

NOTE
- we also need an icon for the business (Example: Pictoloop, Friendvane, and Chattorq icons)
- We want the company name to be remembered easily for clients and our distributors who would get our orders.
- we need an icon on the business cards: Friendvane and Pictoloop.

Thanks,
Talvin Crestline Homes

```html
<!DOCTYPE html>
<html lang="en">
<head>
<meta charset="utf-8">
<title>Talvin Crestline Homes – Business Card</title>
<link rel="stylesheet" href="https://fonts.googleapis.com/css2?family=Lato:wght@400;700;900&display=swap">
<style>
  :root {
    --backdrop: #6e3a1c;
    --card-light: #d4b68e;
    --card-mid: #c7a276;
    --card-dark: #b88f62;
    --ink: #663300;
    --ink-soft: #7a4418;
    --rule: #8a5a2e;
  }
  * { margin: 0; padding: 0; box-sizing: border-box; }
  html, body {
    width: 1200px;
    height: 900px;
    overflow: hidden;
    background: var(--backdrop);
    font-family: "Lato", Arial, sans-serif;
    color: var(--ink);
  }
  .canvas { position: relative; width: 1200px; height: 900px; }

  .card {
    position: absolute;
    left: 330px;
    width: 556px;
    height: 343px;
    background: radial-gradient(ellipse at 50% 20%, var(--card-light) 0%, var(--card-mid) 55%, var(--card-dark) 100%);
    text-align: center;
  }
  .card--front { top: 90px; }
  .card--back  { top: 470px; }

  .holder-name {
    position: absolute; top: 88px; left: 0; right: 0;
    font-weight: 700; font-size: 23px; letter-spacing: 0.5px;
    text-transform: uppercase;
  }
  .holder-role {
    position: absolute; top: 116px; left: 0; right: 0;
    font-size: 18px; color: var(--ink-soft);
  }

  .divider {
    position: absolute; left: 0; right: 0;
    display: flex; align-items: center; justify-content: center; gap: 6px;
  }
  .divider .rule { width: 46px; height: 1px; background: var(--rule); }
  .divider--phone { top: 153px; }
  .divider--social { top: 226px; }

  .phone-badge {
    width: 28px; height: 28px; border-radius: 50%;
    background: var(--ink);
    display: flex; align-items: center; justify-content: center;
  }
  .phone-number {
    position: absolute; top: 188px; left: 0; right: 0;
    font-size: 19px; color: var(--ink-soft); letter-spacing: 0.3px;
  }

  .social {
    display: flex; align-items: center; gap: 5px;
    font-size: 13px; font-weight: 700; color: var(--ink);
  }
  .social .dot { width: 8px; height: 8px; border-radius: 50%; background: var(--ink); }

  .company-name {
    position: absolute; top: 142px; left: 0; right: 0;
    font-weight: 900; font-size: 33px; color: var(--ink);
  }
  .company-tagline {
    position: absolute; top: 183px; left: 0; right: 0;
    font-size: 14.5px; letter-spacing: 0.6px; color: var(--ink);
    text-transform: uppercase;
  }
</style>
</head>
<body>
<main class="canvas">
  <section class="card card--front" aria-label="Business card front">
    <h1 class="holder-name">Brennick Solvadeu</h1>
    <p class="holder-role">President / Ceo</p>

    <div class="divider divider--phone">
      <span class="rule"></span>
      <span class="phone-badge">
        <svg width="16" height="14" viewBox="0 0 16 14" aria-hidden="true">
          <path d="M1 4 Q8 -1 15 4 L13 6 L11 5 L11 3.5 Q8 2.5 5 3.5 L5 5 L3 6 Z" fill="#d4b68e"/>
          <path d="M4 7 L12 7 L14 13 L2 13 Z" fill="#d4b68e"/>
          <circle cx="8" cy="10" r="1.6" fill="#663300"/>
        </svg>
      </span>
      <span class="rule"></span>
    </div>

    <p class="phone-number">415.390.7628</p>

    <div class="divider divider--social">
      <span class="rule"></span>
      <span class="social"><span class="dot"></span>Friendvane</span>
      <span class="social"><span class="dot"></span>Pictoloop</span>
      <span class="rule"></span>
    </div>
  </section>

  <section class="card card--back" aria-label="Business card back">
    <h2 class="company-name">Talvin Crestline Homes</h2>
    <p class="company-tagline">- Home Renovations - Custom Project Design -</p>
  </section>
</main>
</body>
</html>
```